Rocket business card

Modern business card design, use of color is good with clean space too.

Things to include on card:

Quote: I add fuel to your optometry practice

- Eyewear Sales
- Admin Duties
- Revenue Collection
- Leadership
- Tech Adoption
- COGS Reduction
- Product Sourcing
-Medical Growth

Dalton Vessey, CEO
Glint Harbor
Text Me! 847-302-1964
dalton@glintharbor.example

```html
<!DOCTYPE html>
<html lang="en">
<head>
<meta charset="utf-8">
<title>Glint Harbor Business Card</title>
<link rel="stylesheet" href="https://fonts.googleapis.com/css2?family=Roboto:wght@400;500&display=swap">
<style>
  :root {
    --page: #e6e6e6;
    --card: #ffffff;
    --ink: #111111;
    --black: #0c0c0c;
    --red: #e03a2e;
    --orange: #f07a24;
    --amber: #f7b531;
  }
  * { box-sizing: border-box; margin: 0; padding: 0; }
  html, body { width: 1200px; height: 1200px; overflow: hidden; }
  body {
    background: var(--page);
    font-family: "Roboto", Arial, sans-serif;
    color: var(--ink);
    display: flex;
    flex-direction: column;
    align-items: center;
    justify-content: center;
    gap: 48px;
  }
  .card {
    position: relative;
    width: 880px;
    height: 503px;
    background: var(--card);
    overflow: hidden;
    box-shadow: 0 6px 18px rgba(0,0,0,.18);
  }
  .card-back .backdrop { position: absolute; inset: 0; }
  .service-list {
    position: absolute;
    left: 60px;
    top: 62px;
    list-style: none;
    display: flex;
    flex-direction: column;
    gap: 14px;
  }
  .service-list li {
    display: flex;
    align-items: center;
    gap: 16px;
    font-size: 25px;
    letter-spacing: .3px;
  }
  .bullet {
    width: 22px; height: 22px; border-radius: 50%;
    background: linear-gradient(90deg, var(--red), var(--amber));
    border: 3px solid var(--black);
    flex: none;
  }
  .card-front {
    display: flex;
    align-items: center;
    padding: 0 60px 0 70px;
  }
  .brand {
    width: 390px;
    display: flex;
    flex-direction: column;
    align-items: center;
    gap: 26px;
  }
  .brand-mark {
    width: 110px; height: 110px; border-radius: 50%;
    background: linear-gradient(90deg, var(--red), var(--orange) 55%, var(--amber));
  }
  .brand-name {
    font-size: 54px;
    font-weight: 400;
    letter-spacing: 3px;
    text-transform: uppercase;
  }
  .divider {
    width: 2px; height: 220px; background: var(--ink);
    margin: 0 48px 0 30px;
  }
  .contact .person {
    font-size: 36px;
    font-weight: 500;
    text-transform: uppercase;
    letter-spacing: .5px;
    margin-bottom: 14px;
  }
  .contact .line {
    display: flex; align-items: center; gap: 14px;
    font-size: 23px; margin-top: 8px;
  }
  .contact svg { flex: none; }
</style>
</head>
<body>
  <section class="card card-back">
    <svg class="backdrop" width="880" height="503" viewBox="0 0 880 503">
      <defs>
        <linearGradient id="rocketGlow" x1="0" y1="0" x2="1" y2="0">
          <stop offset="0" stop-color="#e03a2e"/>
          <stop offset=".55" stop-color="#f07a24"/>
          <stop offset="1" stop-color="#f7b531"/>
        </linearGradient>
      </defs>
      <path d="M320 0 H880 V430 Q860 503 720 503 H600 C500 470 470 380 470 250 C470 110 420 30 320 0 Z" fill="#0c0c0c"/>
      <circle cx="690" cy="250" r="212" fill="#ffffff"/>
      <circle cx="690" cy="250" r="192" fill="url(#rocketGlow)" role="img" aria-label="Rocket emblem area"/>
    </svg>
    <ul class="service-list">
      <li><span class="bullet"></span>Eyewear Sales</li>
      <li><span class="bullet"></span>Admin Duties</li>
      <li><span class="bullet"></span>Revenue Collection</li>
      <li><span class="bullet"></span>Leadership</li>
      <li><span class="bullet"></span>Tech Adoption</li>
      <li><span class="bullet"></span>COGS Reduction</li>
      <li><span class="bullet"></span>Product Sourcing</li>
      <li><span class="bullet"></span>Medical Growth</li>
    </ul>
  </section>

  <section class="card card-front">
    <div class="brand">
      <div class="brand-mark"></div>
      <div class="brand-name">Glint Harbor</div>
    </div>
    <div class="divider"></div>
    <div class="contact">
      <div class="person">Dalton Vessey, CEO</div>
      <div class="line">
        <svg width="26" height="24" viewBox="0 0 26 24" aria-hidden="true">
          <path d="M3 2 H23 Q25 2 25 4 V15 Q25 17 23 17 H11 L5 22 V17 H3 Q1 17 1 15 V4 Q1 2 3 2 Z" fill="#f07a24"/>
          <circle cx="8" cy="9.5" r="1.6" fill="#fff"/><circle cx="13" cy="9.5" r="1.6" fill="#fff"/><circle cx="18" cy="9.5" r="1.6" fill="#fff"/>
        </svg>
        <span>Text Me! 847-302-1964</span>
      </div>
      <div class="line">
        <svg width="26" height="20" viewBox="0 0 26 20" aria-hidden="true">
          <rect x="1" y="2" width="24" height="16" fill="#f07a24"/>
          <path d="M1 2 L13 11 L25 2" fill="none" stroke="#fff" stroke-width="2"/>
        </svg>
        <span>dalton@glintharbor.example</span>
      </div>
    </div>
  </section>
</body>
</html>
```